6X6 Modern and Professional Postcard for home furnishing company

We are a modern furniture company that is introducing a new product line. It is a new dining collection. We are sending out a 6x6 Postcard to all of our clients introducing the new line. We need to create a 6x6 postcard that is creative, professional, clean, visually attractive and very modern. We are open to possibly using a tagline although we have not thought of one yet. I have attached the template for the postcard and our product images that we are considering to use on the postcard. The following text is the only text that will be on the postcard:1) "Presenting the 2019 Q-Lorvat Dining Collection"2) the tagline, if it works and if we decide to use it3) our website, bmodern.com4) our Instagram, @qlorvatsd

Industry/Entity Type

Home Furnishing

Font styles to use
Sans Serif

Requirements
Must have
• Modern, clean, visually appealing and professional look
Nice to have
• Tagline

```html
<!DOCTYPE html>
<html lang="en">
<head>
<meta charset="utf-8">
<title>Q-Lorvat — 2019 Dining Collection Postcard</title>
<link rel="stylesheet" href="https://fonts.googleapis.com/css2?family=Montserrat:wght@300;400;700;800&display=swap">
<style>
  :root {
    --page: #ededed;
    --paper: #ffffff;
    --ink: #111111;
    --ink-soft: #3a3a3a;
    --photo-sky: #b9c9d6;
    --photo-room: #e7e9ea;
    --photo-floor: #8a8d90;
    --banner-dark: #1c1c1c;
    --banner-mid: #6f7275;
    --banner-light: #d9dadb;
    --steel-blue: #3d5f7d;
    --steel-grey: #9a9ea2;
    --soft-white: #f3f4f5;
  }
  * { margin: 0; padding: 0; box-sizing: border-box; }
  html, body { width: 1200px; height: 1200px; overflow: hidden; background: var(--page); }
  body { font-family: "Montserrat", Arial, sans-serif; color: var(--ink); }

  .spread { position: relative; width: 1200px; height: 1200px; }
  .card { position: absolute; top: 320px; width: 560px; height: 560px; background: var(--paper); overflow: hidden; }
  .card-front { left: 27px; }
  .card-back { left: 613px; }

  /* Front */
  .brand { position: absolute; left: 37px; top: 33px; display: flex; align-items: center; gap: 9px; }
  .brand-mark { width: 26px; height: 26px; background: var(--ink); }
  .brand-name { font-size: 16px; font-weight: 700; color: var(--ink); }

  .intro { position: absolute; right: 38px; top: 88px; font-size: 20px; font-weight: 300; letter-spacing: 4px; text-transform: uppercase; color: var(--ink-soft); white-space: nowrap; }

  .headline { position: absolute; left: 30px; top: 122px; display: flex; align-items: center; gap: 14px; white-space: nowrap; }
  .headline-year { font-size: 86px; font-weight: 800; line-height: 1; letter-spacing: -2px; }
  .headline-title { text-transform: uppercase; font-size: 26px; line-height: 1.08; }
  .headline-title .line-strong { display: block; font-weight: 700; }
  .headline-title .line-light { display: block; font-weight: 300; }

  .photo-backing { position: absolute; left: 0; top: 219px; width: 121px; height: 233px; background: var(--ink); }
  .hero-photo {
    position: absolute; left: 51px; top: 238px; width: 509px; height: 196px;
    background: linear-gradient(180deg, var(--photo-sky) 0%, var(--photo-room) 55%, var(--photo-floor) 100%);
  }

  .contact { position: absolute; left: 0; right: 0; top: 497px; display: flex; justify-content: center; gap: 40px; font-size: 12px; font-weight: 400; color: var(--ink-soft); white-space: nowrap; }
  .contact-item { display: flex; align-items: center; gap: 7px; }
  .contact-dot { width: 13px; height: 13px; border-radius: 50%; background: var(--ink-soft); }

  /* Back */
  .feature-banner {
    position: absolute; left: 0; top: 0; width: 560px; height: 190px;
    background: linear-gradient(135deg, var(--banner-dark) 0%, var(--banner-mid) 45%, var(--banner-light) 100%);
  }
  .product-row { position: absolute; left: 30px; width: 500px; display: flex; justify-content: space-between; }
  .product-row-upper { top: 215px; height: 110px; }
  .product-row-lower { top: 345px; height: 120px; }
  .product-shot { width: 240px; height: 100%; }
  .shot-steel { background: linear-gradient(160deg, var(--soft-white) 0%, var(--steel-grey) 100%); }
  .shot-blue { background: linear-gradient(160deg, var(--soft-white) 0%, var(--steel-blue) 100%); }
  .shot-white { background: linear-gradient(180deg, var(--soft-white) 0%, var(--banner-light) 100%); }
</style>
</head>
<body>
  <main class="spread">
    <section class="card card-front">
      <header class="brand">
        <span class="brand-mark"></span>
        <span class="brand-name">Q-Lorvat</span>
      </header>

      <p class="intro">Presenting the</p>

      <h1 class="headline">
        <span class="headline-year">2019</span>
        <span class="headline-title">
          <span class="line-strong">Q-Lorvat Dining</span>
          <span class="line-light">Collection</span>
        </span>
      </h1>

      <div class="photo-backing"></div>
      <div class="hero-photo" role="img" aria-label="Photo of a white modern dining table and chairs in a bright room with an ocean view"></div>

      <footer class="contact">
        <span class="contact-item"><span class="contact-dot"></span>www.qlorvat.example</span>
        <span class="contact-item"><span class="contact-dot"></span>@qlorvatsd</span>
      </footer>
    </section>

    <section class="card card-back">
      <div class="feature-banner" role="img" aria-label="Photo of a long white dining table with angled steel legs against a dark backdrop"></div>

      <div class="product-row product-row-upper">
        <div class="product-shot shot-steel" role="img" aria-label="Photo of grey extendable dining tables with sculpted bases"></div>
        <div class="product-shot shot-blue" role="img" aria-label="Photo of blue-grey dining tables with sculpted bases"></div>
      </div>

      <div class="product-row product-row-lower">
        <div class="product-shot shot-white" role="img" aria-label="Photo of white dining tables with chrome frame legs"></div>
        <div class="product-shot shot-white" role="img" aria-label="Photo of a white table with a folded steel base and an open frame console"></div>
      </div>

      <footer class="contact">
        <span class="contact-item"><span class="contact-dot"></span>www.qlorvat.example</span>
        <span class="contact-item"><span class="contact-dot"></span>@qlorvatsd</span>
      </footer>
    </section>
  </main>
</body>
</html>
```